Social media design templates

A variety of templates incorporating our logo and colours to use for our postings on different social media platforms. Must be user friendly and meet our brand image. We have attached our logo to view. We would like some of the templates to offer the ability to insert a background image and others to be a template designed around our logo.

We are black and white in colour, and our values speak to our transparency and honesty, so we are looking for clean cut, sharp straight lines, not using any other colours or curved lines.

We are a recruitment company that will be using these templates
- job posting,
- general announcements,
- blog,
- company newsletter,
- updates,
- testimonials and
- top candidate profiles

We would like a gallery of templates to choose from to use separately that all represent our brand.

```html
<!DOCTYPE html>
<html lang="en">
<head>
<meta charset="utf-8">
<title>Ardent Hire – Social Templates</title>
<link href="https://fonts.googleapis.com/css2?family=Montserrat:wght@800&family=Outfit:wght@300;400;500;600&display=swap" rel="stylesheet">
<style>
:root{
  --bg:#7f7f7f;
  --black:#000;
  --ink:#1a1a1a;
  --white:#fff;
  --grey:#6a6a6a;
  --muted:#8a8a8a;
}
*{margin:0;padding:0;box-sizing:border-box}
html,body{width:709px;height:1200px;overflow:hidden;background:var(--bg)}
body{position:relative;font-family:"Outfit",sans-serif;font-weight:300}
.tpl{position:absolute;overflow:hidden}
.abs{position:absolute}
.head{font-family:"Montserrat",sans-serif;font-weight:800;letter-spacing:.06em;line-height:1.2}
.body-copy{font-size:6.5px;line-height:9.3px;letter-spacing:.05em;font-weight:300}
.brand{position:absolute;display:flex;align-items:center;gap:4px;font-family:"Outfit",sans-serif;font-weight:500;letter-spacing:.08em;white-space:nowrap}
.brand .mark{display:block;border:1px solid currentColor}
.photo-portrait{background:linear-gradient(160deg,#6b6a5a 0%,#2c2a30 45%,#1f2f5a 100%)}
.photo-meeting{background:linear-gradient(110deg,#ece8e4 0%,#cfc8c4 35%,#6c6670 62%,#2b3452 100%)}
.photo-person{background:linear-gradient(180deg,#f2f2f2 0%,#e6e4e4 60%,#2a2a2a 100%)}

/* candidate profile */
.profile{left:27px;width:386px;height:248px}
.profile .pic{left:16px;top:16px;width:179px;height:215px}
.profile .title{left:214px;top:34px;font-size:15px}
.profile .name{left:214px;top:88px;font-size:11.5px;font-weight:600;letter-spacing:.1em}
.profile .text{left:214px;top:112px;width:162px}
.profile .brand{left:214px;top:214px;font-size:6.5px}
.profile .brand .mark{width:18px;height:18px}
.profile--light{top:34px;background:var(--white);color:var(--black)}
.profile--light .name{color:var(--grey)}
.profile--light .brand{color:var(--muted)}
.profile--dark{top:305px;background:var(--black);color:var(--white)}
.profile--dark .brand{color:var(--muted)}

/* announcements */
.news{left:432px;width:248px;height:285px}
.news .box{left:41px;top:43px;width:167px;height:200px;padding:18px 10px 0 17px}
.news .title{font-size:12.2px;letter-spacing:.08em}
.news .text{margin-top:8px;font-size:7.6px;line-height:10.8px;letter-spacing:.06em;font-weight:300;white-space:nowrap}
.news .btn{position:absolute;left:44px;top:166px;width:85px;height:20px;display:flex;align-items:center;justify-content:center;gap:6px;font-size:7px;letter-spacing:.1em;font-weight:400}
.news .corner{right:13px;top:251px;width:31px;height:19px;border:1px solid var(--white)}
.news--dark{top:34px}
.news--dark .box{background:rgba(0,0,0,.92);color:var(--white)}
.news--dark .btn{border:1px solid var(--white)}
.news--light{top:341px}
.news--light .box{background:rgba(255,255,255,.93);color:var(--black)}
.news--light .btn{border:1px solid var(--black)}

/* recruiting */
.hiring{left:27px;width:383px;height:267px}
.hiring .pic{left:171px;top:0;width:212px;height:267px}
.hiring .title{font-size:27px;letter-spacing:.05em;line-height:1.05;white-space:nowrap}
.hiring .text{font-size:10.5px;line-height:16.7px;letter-spacing:.07em;font-weight:300;white-space:nowrap}
.hiring .brand{font-size:7px;color:var(--white)}
.hiring .brand .mark{width:20px;height:20px}
.hiring--light{top:579px;background:var(--white)}
.hiring--light .panel{left:23px;top:26px;width:228px;height:216px;background:rgba(26,26,26,.96);color:var(--white)}
.hiring--light .brand{left:22px;top:22px}
.hiring--light .title{position:absolute;left:24px;top:62px}
.hiring--light .text{position:absolute;left:24px;top:127px}
.hiring--dark{top:876px;background:var(--black);color:var(--white)}
.hiring--dark .shade{left:171px;top:26px;width:80px;height:216px;background:rgba(0,0,0,.85)}
.hiring--dark .brand{left:38px;top:42px}
.hiring--dark .title{position:absolute;left:38px;top:90px}
.hiring--dark .text{position:absolute;left:38px;top:152px}

/* testimonial */
.review{left:432px;width:248px;height:248px;background:var(--white)}
.review .band{left:0;top:0;width:248px;height:107px;background:var(--black)}
.review .title{top:40px;width:100%;text-align:center;color:var(--white);font-size:12px;letter-spacing:.5em;padding-left:.5em}
.review .pic{left:92px;top:70px;width:65px;height:64px;border:2px solid var(--white)}
.review .text{left:27px;top:150px;width:205px;font-size:5.8px;line-height:10.3px;color:var(--ink);font-weight:400}
.review .name{top:204px;width:100%;text-align:center;font-size:8px;font-weight:600;color:var(--muted)}
.review .brand{left:169px;top:218px;font-size:5px;color:var(--grey)}
.review .brand .mark{width:14px;height:14px}
.review--a{top:648px}
.review--b{top:917px}
</style>
</head>
<body>

<section class="tpl profile profile--light">
  <div class="abs pic photo-portrait" role="img" aria-label="Portrait of a candidate in a blue suit adjusting his tie"></div>
  <h2 class="abs head title">TOP CANDIDATE<br>PROFILE</h2>
  <p class="abs name">Daniel Reyes, 36</p>
  <p class="abs body-copy text">Lorem ipsum dolor sit amet, consectetur adipiscing elit, sed do eiusmod tempor incididunt ut labore et dolore magna aliqua. Quis ipsum suspendisse ultrices gravida. Risus commodo viverra maecenas accumsan lacus vel facilisis. Lorem ipsum dolor sit amet, consectetur adipiscing elit, sed do eiusmod tempor incididunt ut labore et dolore magna aliqua. Quis ipsum suspendisse ultrices gravida. Risus</p>
  <div class="brand"><span class="mark"></span>ARDENT HIRE</div>
</section>

<section class="tpl profile profile--dark">
  <div class="abs pic photo-portrait" role="img" aria-label="Portrait of a candidate in a blue suit adjusting his tie"></div>
  <h2 class="abs head title">TOP CANDIDATE<br>PROFILE</h2>
  <p class="abs name">Daniel Reyes, 36</p>
  <p class="abs body-copy text">Lorem ipsum dolor sit amet, consectetur adipiscing elit, sed do eiusmod tempor incididunt ut labore et dolore magna aliqua. Quis ipsum suspendisse ultrices gravida. Risus commodo viverra maecenas accumsan lacus vel facilisis. Lorem ipsum dolor sit amet, consectetur adipiscing elit, sed do eiusmod tempor incididunt ut labore et dolore magna aliqua. Quis ipsum suspendisse ultrices gravida. Risus</p>
  <div class="brand"><span class="mark"></span>ARDENT HIRE</div>
</section>

<section class="tpl news news--dark photo-meeting" role="img" aria-label="Background photo of two businessmen reviewing documents at a table">
  <div class="abs box">
    <h2 class="head title">GENERAL<br>ANNOUNCEMENTS</h2>
    <p class="text">Lorem ipsum dolor sit amet,<br>consectetur adipiscing elit, sed<br>do eiusmod tempor incididunt ut<br>labore et dolore magna aliqua.<br>Quis ipsum suspendisse ultrices<br>gravida. Risus commodo viverra<br>maecenas accumsan lacus vel<br>Lorem ipsum dolor sit amet,<br>consectetur adipiscing elit, sed</p>
    <div class="btn">READ MORE
      <svg width="7" height="10" viewBox="0 0 7 10"><path d="M3.5 0V9M0.5 6L3.5 9L6.5 6" fill="none" stroke="currentColor" stroke-width="1"/></svg>
    </div>
  </div>
  <div class="abs corner"></div>
</section>

<section class="tpl news news--light photo-meeting" role="img" aria-label="Background photo of two businessmen reviewing documents at a table">
  <div class="abs box">
    <h2 class="head title">GENERAL<br>ANNOUNCEMENTS</h2>
    <p class="text">Lorem ipsum dolor sit amet,<br>consectetur adipiscing elit, sed<br>do eiusmod tempor incididunt ut<br>labore et dolore magna aliqua.<br>Quis ipsum suspendisse ultrices<br>gravida. Risus commodo viverra<br>maecenas accumsan lacus vel<br>Lorem ipsum dolor sit amet,<br>consectetur adipiscing elit, sed</p>
    <div class="btn">READ MORE
      <svg width="7" height="10" viewBox="0 0 7 10"><path d="M3.5 0V9M0.5 6L3.5 9L6.5 6" fill="none" stroke="currentColor" stroke-width="1"/></svg>
    </div>
  </div>
  <div class="abs corner"></div>
</section>

<section class="tpl hiring hiring--light">
  <div class="abs pic photo-meeting" role="img" aria-label="Photo of two smiling businessmen reviewing papers together"></div>
  <div class="abs panel">
    <div class="brand"><span class="mark"></span>ARDENT HIRE</div>
    <h2 class="head title">WE ARE<br>RECRUITING</h2>
    <p class="text">Lorem ipsum dolor sit amet,<br>consectetur adipiscing elit, sed<br>do eiusmod tempor incididunt ut<br>labore et dolore magna aliqua.</p>
  </div>
</section>

<section class="tpl hiring hiring--dark">
  <div class="abs pic photo-meeting" role="img" aria-label="Photo of two smiling businessmen reviewing papers together"></div>
  <div class="abs shade"></div>
  <div class="brand"><span class="mark"></span>ARDENT HIRE</div>
  <h2 class="head title">WE ARE<br>RECRUITING</h2>
  <p class="text">Lorem ipsum dolor sit amet,<br>consectetur adipiscing elit, sed<br>do eiusmod tempor incididunt ut<br>labore et dolore magna aliqua.</p>
</section>

<section class="tpl review review--a">
  <div class="abs band" style="background:linear-gradient(90deg,#0a0a0a,#151515)" role="img" aria-label="Darkened office background photo"></div>
  <h2 class="abs head title">TESTIMONIAL</h2>
  <div class="abs pic photo-person" role="img" aria-label="Headshot of a smiling woman with glasses"></div>
  <p class="abs text">Lorem ipsum dolor sit amet, consectetur adipiscing elit, sed do eiusmod tempor incididunt ut labore et dolore magna aliqua. Quis ipsum suspendisse ultrices gravida. Risus commodo viverra maecenas accumsan lacus vel facilisis. Lorem ipsum dolor sit amet, consectetur adipiscing elit, sed do eiusmod tempor incididunt ut labore et dolore magna aliqua. Quis</p>
  <p class="abs name">Mia Chen</p>
  <div class="brand"><span class="mark"></span>ARDENT HIRE</div>
</section>

<section class="tpl review review--b">
  <div class="abs band"></div>
  <h2 class="abs head title">TESTIMONIAL</h2>
  <div class="abs pic photo-person" role="img" aria-label="Headshot of a smiling woman with glasses"></div>
  <p class="abs text">Lorem ipsum dolor sit amet, consectetur adipiscing elit, sed do eiusmod tempor incididunt ut labore et dolore magna aliqua. Quis ipsum suspendisse ultrices gravida. Risus commodo viverra maecenas accumsan lacus vel facilisis. Lorem ipsum dolor sit amet, consectetur adipiscing elit, sed do eiusmod tempor incididunt ut labore et dolore magna aliqua. Quis</p>
  <p class="abs name">Mia Chen</p>
  <div class="brand"><span class="mark"></span>ARDENT HIRE</div>
</section>

</body>
</html>
```